Dential Clinic Business Card

We need a simple elegant business card. 2 sided. First side with our details, and 2nd side with appointment time rows.

Dark background preferred. Will consider monotone design, or colored. Surprise us.

Details:
SIDE1

Maplewood Square Dental

Dr Peter Hollis
BDSc(Adel) FRZPTA

Shop 42, Maplewood Square
7-19 Birch Parade, Elmridge VIC 3188
Phone: 03 9555 0148
email: info@maplewoodsquaredental.com.au
site: www.maplewoodsquaredental.com.au
_____________________________________
SIDE 2
Appointed Time ________________________
Notes _______________________

Target Market(s)

Dental Patients

Industry/Entity Type

Healthcare

Contact Information for Business Card

SIDE1

Maplewood Square Dental

Dr Peter Hollis
Shop 42, Maplewood Square
Phone: 03 9555 0148
SIDE 2

Font styles to use
Other font styles liked:
• Comfortaa

Requirements
Must have
• Dr Peter Hollis
BDSc(Adel) FRZPTA

Address
Phone
Email
Website
Nice to have
• Simple elegant design with our logo.
Colored logo.
Light text on dark background - Side 1
Light background so can be written on with dark pen - SIde 2
Should not have
• Too many colors

```html
<!DOCTYPE html>
<html lang="en">
<head>
<meta charset="utf-8">
<title>Maplewood Square Dental – Business Card</title>
<link href="https://fonts.googleapis.com/css2?family=Lato:wght@400;700&display=swap" rel="stylesheet">
<style>
  :root {
    --page: #d6d6d6;
    --card-dark: #0f1113;
    --card-light: #ffffff;
    --blue: #1d8fd4;
    --green: #7dc242;
    --grey-text: #b8b8b8;
    --font: "Lato", sans-serif;
  }
  * { box-sizing: border-box; margin: 0; padding: 0; }
  html, body { width: 1200px; height: 1143px; overflow: hidden; }
  body { background: var(--page); font-family: var(--font); position: relative; }

  .card { position: absolute; left: 299px; width: 602px; height: 343px; }
  .card--front { top: 180px; background: var(--card-dark); }
  .card--back { top: 621px; background: var(--card-light); }

  .brand { position: absolute; display: flex; align-items: center; gap: 12px; }
  .brand__dot { width: 34px; height: 34px; border-radius: 50%; background: var(--green); flex: none; }
  .brand__name { font-size: 27px; font-weight: 400; color: var(--green); white-space: nowrap; letter-spacing: 0.3px; }
  .card--front .brand { left: 29px; top: 71px; }
  .card--back .brand { left: 0; right: 0; top: 57px; justify-content: center; }

  .person { position: absolute; left: 29px; top: 196px; }
  .person__name { font-size: 20.5px; font-weight: 700; line-height: 1; }
  .person__name .first { color: var(--blue); }
  .person__name .last { color: var(--green); }
  .person__role { margin-top: 9px; font-size: 13.5px; color: var(--grey-text); }

  .rule { position: absolute; left: 29px; width: 545px; height: 1px; background: var(--blue); }
  .card--front .rule { top: 252px; }
  .card--back .rule { left: 30px; width: 540px; top: 139px; height: 1.5px; }

  .contacts { position: absolute; left: 29px; top: 263px; list-style: none; }
  .contacts li { display: flex; align-items: center; height: 19.5px; font-size: 13.5px; color: var(--grey-text); }
  .contacts svg { width: 13px; height: 13px; margin-right: 11px; flex: none; }

  .address { position: absolute; right: 29px; top: 286px; text-align: right; font-size: 13.5px; line-height: 16px; color: var(--grey-text); font-style: normal; }

  .appointment { position: absolute; left: 30px; right: 32px; top: 162px; display: flex; align-items: center; }
  .appointment__label { font-size: 19px; color: var(--blue); letter-spacing: 0.6px; margin-right: 17px; white-space: nowrap; }
  .days { display: flex; flex: 1; justify-content: space-between; list-style: none; }
  .days li { display: flex; align-items: center; font-size: 14.5px; color: var(--blue); letter-spacing: 1.2px; }
  .days li::before { content: ""; width: 9px; height: 9px; border: 2px solid var(--green); border-radius: 50%; margin-right: 7px; }

  .field { position: absolute; display: flex; align-items: flex-end; }
  .field__label { font-size: 19px; color: var(--blue); line-height: 1; }
  .field__line { height: 1.5px; background: var(--green); margin-bottom: 2px; }
  .field--date { left: 259px; top: 208px; }
  .field--time { left: 259px; top: 241px; }
  .field--date .field__line, .field--time .field__line { position: absolute; left: 57px; width: 226px; bottom: 0; }
  .field--notes { left: 30px; top: 287px; }
  .field--notes .field__line { width: 479px; margin-left: 6px; }
</style>
</head>
<body>

<section class="card card--front" aria-label="Front of business card">
  <div class="brand">
    <span class="brand__dot"></span>
    <span class="brand__name">Maplewood Square Dental</span>
  </div>

  <div class="person">
    <p class="person__name"><span class="first">Dr Peter</span> <span class="last">Hollis</span></p>
    <p class="person__role">Principal Dentist</p>
  </div>

  <div class="rule"></div>

  <ul class="contacts">
    <li>
      <svg viewBox="0 0 16 16" aria-hidden="true"><path fill="#7dc242" d="M1 5c0-2 3-3 7-3s7 1 7 3v1h-4V5H5v1H1z M3 7h10l1 7H2z"/><circle cx="8" cy="10.5" r="2" fill="#0f1113"/></svg>
      03 9555 0148
    </li>
    <li>
      <svg viewBox="0 0 16 16" aria-hidden="true"><rect x="1" y="3" width="14" height="10" fill="#7dc242"/><path d="M1 3l7 6 7-6M1 13l5-5M15 13l-5-5" stroke="#0f1113" stroke-width="1.2" fill="none"/></svg>
      info@maplewoodsquaredental.com.au
    </li>
    <li>
      <svg viewBox="0 0 16 16" aria-hidden="true"><g fill="none" stroke="#7dc242" stroke-width="1.3"><circle cx="8" cy="8" r="6.5"/><ellipse cx="8" cy="8" rx="3" ry="6.5"/><path d="M1.5 8h13M2.5 5h11M2.5 11h11"/></g></svg>
      www.maplewoodsquaredental.com.au
    </li>
  </ul>

  <address class="address">
    Shop 42, Maplewood Square<br>
    7-19 Birch Parade, Elmridge VIC 3188
  </address>
</section>

<section class="card card--back" aria-label="Back of business card">
  <div class="brand">
    <span class="brand__dot"></span>
    <span class="brand__name">Maplewood Square Dental</span>
  </div>

  <div class="rule"></div>

  <div class="appointment">
    <span class="appointment__label">NEXT APPOINTMENT:</span>
    <ul class="days">
      <li>Mon</li><li>Tue</li><li>Wed</li><li>Thur</li><li>Fri</li>
    </ul>
  </div>

  <div class="field field--date"><span class="field__label">Date:</span><span class="field__line"></span></div>
  <div class="field field--time"><span class="field__label">Time:</span><span class="field__line"></span></div>
  <div class="field field--notes"><span class="field__label">Notes:</span><span class="field__line"></span></div>
</section>

</body>
</html>
```